Consultative Employee Benifits Firm Needs Business Card Design Project

We need a business card design for a new company based in Northern Virginia called "Telman Financial Services, LLC. We are both a wealth management advisory firm, as well as an employee benefits firm, which strives to provide superior creativity in employee benefits plan design and greater client and employee satisfaction. We are obsessed with service and follow up.

Our firm specializes in the areas of group health, life, dental, disability, voluntary benefits, Executive Benefits, HRA and HSA programs. We offer competitive employee benefit packages and pricing models for single or multi-state/multi location companies by maintaining preferred relationships with a large number of regional and national carriers.

Our firm also considers the many dimensions of your wealth through an integrated process we call wealth structuring — a comprehensive, dynamic approach to building, preserving, enjoying and transferring your wealth. And because we are often dealing with complex ownership structures and complicated, changing family dynamics, we bring the highest level of experience and creativity to managing your wealth. We work hard to help ensure that your legacy lasts by preparing your children for the financial challenges and opportunities that are headed their way.

Our final design should communicate an integrated approach to finanial safety and optimization
Updates

 Due to a few designers not accepting due to low budget, I have increased budget payout 19%. 

Project Deadline Extended
Reason: I have only heard from 12 designers. So, maybe I did not give the right amount of time to do the project. For the designers that have submitted their designs, thank you. I have seen three or four designs that I liked and might end up with one of them after it's all over, but I thought I would see between 20 - 25 before everything was over. Dan

Target Market(s)

Professionals; doctors, contractors, small to mid size business owners, ages 50 -65 with nert worth of 2MM

Industry/Entity Type

Financial

Requirements
Must have
• Telman Financial Services, LLC

Dan Telman
President
41957 Marwick Hollow Street
Quenford Glen, 20871

Office: 703 555-0184
Cell: 703 555-0127
Fax: 703 555-0163
Email: dantelman@quorvex.net
Should not have
• No pink or yellow colors.
No generic clipart (coins, dollar signs, money bags, graphs)

```html
<!DOCTYPE html>
<html lang="en">
<head>
<meta charset="utf-8">
<title>Telman Financial Services, LLC — Business Card</title>
<link href="https://fonts.googleapis.com/css2?family=Questrial&display=swap" rel="stylesheet">
<style>
  :root {
    --backdrop: #d6d7da;
    --card: #f1f1f1;
    --brand-blue: #3f56a0;
    --mark-grey: #4a4a4c;
    --on-blue: #ffffff;
    --divider: rgba(255,255,255,0.55);
  }
  * { margin: 0; padding: 0; box-sizing: border-box; }
  html, body {
    width: 1200px; height: 534px; overflow: hidden;
    background: var(--backdrop);
    font-family: "Questrial", "Century Gothic", sans-serif;
  }
  .stage { position: relative; width: 1200px; height: 534px; }

  .card {
    position: absolute; top: 119px;
    width: 517px; height: 295px;
    background: var(--card);
    overflow: hidden;
    box-shadow: 0 2px 8px rgba(0,0,0,0.18);
  }
  .card--front { left: 62px; }
  .card--back  { left: 622px; }

  /* Brand name lockup */
  .brand { position: absolute; display: flex; align-items: center; }
  .brand__square { background: var(--mark-grey); flex: none; }
  .brand__name { color: var(--brand-blue); line-height: 1; }
  .brand__line1 { display: block; }
  .brand__line2 { display: block; text-align: right; }

  .card--front .brand { left: 77px; top: 107px; gap: 18px; }
  .card--front .brand__square { width: 84px; height: 84px; }
  .card--front .brand__line1 { font-size: 36px; letter-spacing: -0.3px; }
  .card--front .brand__line2 { font-size: 21px; margin-top: 4px; }

  .card--back .brand { left: 30px; top: 59px; gap: 12px; }
  .card--back .brand__square { width: 56px; height: 56px; }
  .card--back .brand__line1 { font-size: 25px; letter-spacing: -0.2px; }
  .card--back .brand__line2 { font-size: 14.5px; margin-top: 3px; }

  .band { position: absolute; left: 0; right: 0; bottom: 0; background: var(--brand-blue); }
  .card--front .band { height: 26px; }
  .card--back .band { height: 119px; }

  .contact {
    position: absolute; top: 19px; left: 48px; right: 20px;
    display: flex; color: var(--on-blue);
  }
  .contact__person { width: 238px; font-size: 13.5px; line-height: 22.5px; }
  .contact__name { font-size: 17px; letter-spacing: 0.4px; line-height: 20px; margin-bottom: 1px; text-transform: uppercase; }
  .contact__lines {
    border-left: 1px solid var(--divider);
    padding-left: 8px; font-size: 13.5px; line-height: 22.5px;
    margin-top: 2px; height: 84px;
  }
</style>
</head>
<body>
<main class="stage">
  <section class="card card--front" aria-label="Card front">
    <div class="brand">
      <span class="brand__square"></span>
      <div class="brand__name">
        <span class="brand__line1">Telman Financial</span>
        <span class="brand__line2">Services, LLC.</span>
      </div>
    </div>
    <div class="band"></div>
  </section>

  <section class="card card--back" aria-label="Card back">
    <div class="brand">
      <span class="brand__square"></span>
      <div class="brand__name">
        <span class="brand__line1">Telman Financial</span>
        <span class="brand__line2">Services, LLC.</span>
      </div>
    </div>
    <div class="band">
      <div class="contact">
        <div class="contact__person">
          <p class="contact__name">Dan Telman</p>
          <p>President</p>
          <p>41957 Marwick Hollow Street</p>
          <p>Quenford Glen, 20871</p>
        </div>
        <div class="contact__lines">
          <p>Office: 703 555-0184</p>
          <p>Cell: 703 555-0127</p>
          <p>Fax: 703 555-0163</p>
          <p>Email: dantelman@quorvex.net</p>
        </div>
      </div>
    </div>
  </section>
</main>
</body>
</html>
```